Letterhead and Envelopes design using existing logo. Logo can be found at tlventures.net

Use existing logo (attached) and incorporate in letterhead and envelope designs.

Current logo can be viewed at tlventures.net the web site reflect various parent and sub companies. Please see attached as well.

Target Market(s)

Other oil and gas operators.

Industry/Entity Type

Oil And Gas

Font styles to use
Sans Serif

Colors

Designer to choose colors to be used in the design.

Requirements
Must have
• Current logo and address
Nice to have
• Modern, contemporary approach yet incorporate existing traditional design.
• After design is selected for Ridgemont Caldera Holdings I will use similar design for Royalties, Exploration, Energy and Farms with different color schemes.

```html
<!DOCTYPE html>
<html lang="en">
<head>
<meta charset="utf-8">
<title>Ridgemont Caldera Holdings — Letterhead</title>
<link href="https://fonts.googleapis.com/css2?family=Arimo:wght@400;700&display=swap" rel="stylesheet">
<style>
  :root {
    --backdrop: #d9d9d9;
    --paper: #ffffff;
    --brand-green: #6f9a3f;
    --soft-grey: #e5e5e5;
    --ink: #1a1a1a;
    --ink-light: #ffffff;
  }
  * { margin: 0; padding: 0; box-sizing: border-box; }
  html, body {
    width: 1200px;
    height: 1200px;
    overflow: hidden;
    background: var(--backdrop);
    font-family: "Arimo", Arial, sans-serif;
  }
  .letterhead {
    position: absolute;
    left: 200px;
    top: 60px;
    width: 800px;
    height: 1080px;
    background: var(--paper);
    overflow: hidden;
    box-shadow: 0 6px 24px rgba(0,0,0,0.18);
  }
  .letterhead__shapes {
    position: absolute;
    inset: 0;
    width: 100%;
    height: 100%;
  }
  .shape-green { fill: var(--brand-green); }
  .shape-grey { fill: var(--soft-grey); }

  .brand {
    position: absolute;
    left: 30px;
    top: 58px;
    display: flex;
    align-items: center;
    gap: 10px;
  }
  .brand__dot {
    width: 22px;
    height: 22px;
    border-radius: 50%;
    background: var(--brand-green);
  }
  .brand__name {
    font-size: 17px;
    font-weight: 700;
    color: var(--ink);
    letter-spacing: 0.02em;
  }

  .address {
    position: absolute;
    left: 535px;
    top: 48px;
    display: flex;
    align-items: flex-start;
    gap: 10px;
    color: var(--ink-light);
    font-size: 13px;
    line-height: 1.35;
  }
  .icon { width: 14px; height: 14px; flex: none; margin-top: 2px; }
  .icon--pin { fill: var(--ink); }
  .icon--green { fill: var(--brand-green); }

  .contact {
    position: absolute;
    left: 590px;
    top: 990px;
    display: flex;
    flex-direction: column;
    gap: 8px;
    font-size: 13px;
    color: var(--ink);
  }
  .contact__row { display: flex; align-items: center; gap: 10px; }
  .contact__row .icon { margin-top: 0; }
</style>
</head>
<body>
  <main class="letterhead">
    <svg class="letterhead__shapes" viewBox="0 0 800 1080" preserveAspectRatio="none" aria-hidden="true">
      <path class="shape-green" d="M375 0 H800 V150 C745 190 690 207 610 207 C480 207 400 140 388 60 Z"/>
      <path class="shape-grey" d="M88 1080 C70 930 120 770 330 755 C440 750 510 800 530 870 C548 950 555 1030 590 1080 Z"/>
    </svg>

    <div class="brand">
      <span class="brand__dot"></span>
      <span class="brand__name">Ridgemont Caldera Holdings</span>
    </div>

    <div class="address">
      <svg class="icon icon--pin" viewBox="0 0 24 24"><path d="M12 2a7 7 0 0 0-7 7c0 5 7 13 7 13s7-8 7-13a7 7 0 0 0-7-7zm0 9.5A2.5 2.5 0 1 1 12 6.5a2.5 2.5 0 0 1 0 5z"/></svg>
      <p>PO Box 418 Glendive<br>Montana 59330</p>
    </div>

    <div class="contact">
      <div class="contact__row">
        <svg class="icon icon--green" viewBox="0 0 24 24"><path d="M3 9c0-3 4-5 9-5s9 2 9 5v2h-5V8.5c-1-.5-2.5-.8-4-.8s-3 .3-4 .8V11H3zM6 12h12l2 8H4z"/></svg>
        <span>(406) 555.0142</span>
      </div>
      <div class="contact__row">
        <svg class="icon icon--green" viewBox="0 0 24 24"><path d="M22 2 2 10l7 3 3 9z"/></svg>
        <span>reception@tlventures.net</span>
      </div>
    </div>
  </main>
</body>
</html>
```